Consulting group
Business cards and stationary
Use same font as used in my logo
I think it is Swiss721?
Simple
Damon Fairley
President
417 W. Marlow Avenue, Apt 118 Ann Arbor, MI 48177
Damon@DamonFairley.com
www.TheCopperLantern.com
Looking for envelope, letterhead, and business card.
the logo? if you want to try putting a quote on it: "“The worst thing that can happen to a good cause is, not to be skillfully attacked, but to be ineptly defended.” - Corvelle. Not sure if I will like the quote on there or not.

```html
<!DOCTYPE html>
<html lang="en">
<head>
<meta charset="utf-8">
<title>The Copper Lantern — Business Cards</title>
<link href="https://fonts.googleapis.com/css2?family=Playfair+Display:wght@400;700&display=swap" rel="stylesheet">
<style>
  :root {
    --brand-red: #e4161b;
    --paper: #ffffff;
    --ink: #1c1c1c;
    --backdrop: #e9e9e7;
    --shadow: rgba(0, 0, 0, 0.18);
  }
  * { box-sizing: border-box; margin: 0; padding: 0; }
  html, body {
    width: 1200px;
    height: 647px;
    overflow: hidden;
    background: var(--backdrop);
    font-family: "Playfair Display", Georgia, serif;
  }
  .stage {
    width: 1200px;
    height: 647px;
    display: flex;
    align-items: center;
    justify-content: center;
    gap: 60px;
  }
  .card {
    width: 500px;
    height: 290px;
    border-radius: 18px;
    overflow: hidden;
    box-shadow: 0 10px 28px var(--shadow);
    display: flex;
  }
  /* Front */
  .card-front .logo-side {
    width: 50%;
    background: var(--paper);
    display: flex;
    align-items: center;
    justify-content: center;
  }
  .card-front .contact-side {
    width: 50%;
    background: var(--brand-red);
    color: var(--paper);
    padding: 40px 26px 0 28px;
  }
  .wordmark {
    display: flex;
    align-items: center;
    gap: 14px;
    color: var(--brand-red);
  }
  .wordmark .mark-square {
    width: 44px;
    height: 44px;
    background: currentColor;
    flex: none;
  }
  .wordmark .name {
    font-weight: 400;
    font-size: 30px;
    line-height: 1.0;
  }
  .contact-side .person {
    font-weight: 700;
    font-size: 16px;
  }
  .contact-side .role {
    font-size: 11px;
    margin-bottom: 22px;
  }
  .contact-side .address {
    font-size: 11px;
    line-height: 1.45;
    margin-bottom: 14px;
  }
  .contact-list { list-style: none; }
  .contact-list li {
    display: flex;
    align-items: center;
    gap: 8px;
    font-size: 11px;
    line-height: 1.9;
  }
  .contact-list svg { width: 11px; height: 11px; flex: none; }
  /* Back */
  .card-back {
    background: var(--brand-red);
    align-items: center;
    justify-content: center;
  }
  .card-back .wordmark { color: var(--paper); }
  .card-back .wordmark .name { font-size: 38px; }
  .card-back .wordmark .mark-square { width: 56px; height: 56px; }
</style>
</head>
<body>
<main class="stage">
  <section class="card card-front" aria-label="Business card front">
    <div class="logo-side">
      <div class="wordmark">
        <span class="mark-square"></span>
        <span class="name">The<br>Copper<br>Lantern</span>
      </div>
    </div>
    <div class="contact-side">
      <p class="person">Damon Fairley</p>
      <p class="role">President</p>
      <p class="address">417 W. Marlow Avenue, Apt 118<br>Ann Arbor, MI 48177</p>
      <ul class="contact-list">
        <li>
          <svg viewBox="0 0 12 12" aria-hidden="true"><path d="M2.5 1h2l1 3-1.3 1a6 6 0 0 0 2.8 2.8L8 6.5l3 1v2a1.5 1.5 0 0 1-1.5 1.5A8.5 8.5 0 0 1 1 2.5 1.5 1.5 0 0 1 2.5 1z" fill="currentColor"/></svg>
          (734) 555-0142
        </li>
        <li>
          <svg viewBox="0 0 12 12" aria-hidden="true"><rect x="0.8" y="2.3" width="10.4" height="7.4" fill="none" stroke="currentColor" stroke-width="1.2"/><path d="M1 2.6l5 4 5-4" fill="none" stroke="currentColor" stroke-width="1.2"/></svg>
          Damon@DamonFairley.com
        </li>
        <li>
          <svg viewBox="0 0 12 12" aria-hidden="true"><circle cx="6" cy="6" r="5" fill="none" stroke="currentColor" stroke-width="1.1"/><path d="M1 6h10M6 1c-2.5 3-2.5 7 0 10M6 1c2.5 3 2.5 7 0 10" fill="none" stroke="currentColor" stroke-width="0.9"/></svg>
          www.TheCopperLantern.com
        </li>
      </ul>
    </div>
  </section>

  <section class="card card-back" aria-label="Business card back">
    <div class="wordmark">
      <span class="mark-square"></span>
      <span class="name">The<br>Copper<br>Lantern</span>
    </div>
  </section>
</main>
</body>
</html>
```